Brightfield Yard Service and Beyond LLC

• Mowing
• Weed eating
•Edging
• hedge trimming
• landscaping
•mulching
•yard clean up
• pressure washing

Target Market(s)

Everyone

Contact Information for Business Card

Licensed and insured

Font styles to use
Serif

Colors
59FF00
82FF00
B8FF75
E3FFCB
F4FFEA
F0912C
F2A743
F7CA91
FBE8D2
FDF5EE
EE7325
F08F49
F5BC92
FAE3D3
FDF4ED
EB3D1F
EC4F4E
F09395
F8D3D4
FCEDEE
E54698
E96AAD
F1A4CE
F9D9EA
FCEFF6

```html
<!DOCTYPE html>
<html lang="en">
<head>
<meta charset="utf-8">
<title>Brightfield Yard Service and Beyond LLC – Business Card</title>
<link rel="stylesheet" href="https://fonts.googleapis.com/css2?family=Cinzel:wght@600;700&family=Poppins:wght@400;500&display=swap">
<style>
  :root {
    --stage: #2b2b2b;
    --card-white: #ffffff;
    --brand-green: #2b7c00;
    --back-green: #2c7d00;
    --grass-light: #3f9a0c;
    --grass-faint: #e9f1e2;
    --accent-orange: #e8761f;
    --ink: #1c1c1c;
    --muted: #555555;
    --on-green: #ffffff;
  }
  * { margin: 0; padding: 0; box-sizing: border-box; }
  html, body { width: 1093px; height: 1200px; overflow: hidden; }
  body { background: var(--stage); position: relative; font-family: "Poppins", sans-serif; }

  .card {
    position: absolute;
    left: 265px;
    width: 580px;
    height: 356px;
    border-radius: 28px;
    overflow: hidden;
    box-shadow: 0 4px 6px rgba(0,0,0,.55);
  }
  .card--front { top: 226px; background: var(--card-white); }
  .card--back { top: 621px; background: var(--back-green); }

  .grass-deco {
    position: absolute;
    left: 0; top: 110px;
    width: 190px; height: 246px;
    background: radial-gradient(ellipse 100% 100% at 35% 100%, var(--grass-faint) 0%, rgba(233,241,226,.7) 55%, rgba(233,241,226,0) 100%);
  }

  .brand { position: absolute; line-height: 1; }
  .brand__primary { display: block; font-family: "Cinzel", serif; font-weight: 700; font-size: 42px; letter-spacing: 1px; }
  .brand__secondary { display: block; font-family: "Poppins", sans-serif; font-weight: 500; font-size: 15.5px; letter-spacing: 1.6px; margin-top: 7px; white-space: nowrap; }

  .card--front .brand { right: 34px; top: 60px; text-align: right; }
  .card--front .brand__primary { color: var(--brand-green); }
  .card--front .brand__secondary { color: var(--accent-orange); }
  .card--back .brand { left: 0; right: 0; top: 99px; text-align: center; color: var(--on-green); }

  .tagline {
    position: absolute;
    display: flex; align-items: center; gap: 7px;
    font-size: 13.5px; font-weight: 500; letter-spacing: 1.3px; text-transform: uppercase;
    white-space: nowrap;
  }
  .tagline::before, .tagline::after { content: ""; width: 50px; height: 1.5px; background: currentColor; }
  .card--front .tagline { right: 34px; top: 126px; color: var(--muted); }
  .card--back .tagline { left: 50%; transform: translateX(-50%); top: 166px; color: var(--on-green); }

  .person { position: absolute; left: 36px; top: 180px; right: 34px; }
  .person__name { font-family: "Cinzel", serif; font-weight: 600; font-size: 23px; color: var(--brand-green); letter-spacing: .5px; line-height: 1.1; }
  .person__role-row { display: flex; align-items: center; gap: 10px; margin-top: 2px; }
  .person__role { font-size: 16.5px; color: var(--ink); white-space: nowrap; }
  .person__rule { flex: 1; height: 1.5px; background: var(--accent-orange); margin-top: 2px; }

  .contact { position: absolute; left: 36px; top: 258px; list-style: none; }
  .contact__item { display: flex; align-items: center; gap: 7px; font-size: 16.5px; color: var(--ink); height: 21px; }
  .contact__icon { width: 16px; height: 16px; flex: none; }
  .contact__highlight { color: var(--brand-green); }

  .address { position: absolute; right: 34px; top: 280px; text-align: right; font-size: 16.5px; line-height: 21px; color: var(--ink); font-style: normal; }

  .services { position: absolute; left: 0; right: 0; top: 247px; text-align: center; color: var(--on-green); font-size: 17.5px; line-height: 28px; }

  .grass-band {
    position: absolute; left: 0; right: 0; bottom: 0; height: 40px;
    background: linear-gradient(180deg, var(--back-green) 0%, var(--grass-light) 100%);
  }
</style>
</head>
<body>

  <section class="card card--front" aria-label="Business card front">
    <div class="grass-deco" role="img" aria-label="Faint grass blades decoration"></div>

    <h1 class="brand">
      <span class="brand__primary">BRIGHTFIELD</span>
      <span class="brand__secondary">YARD SERVICE AND BEYOND LLC</span>
    </h1>
    <p class="tagline">Licensed and insured</p>

    <div class="person">
      <p class="person__name">Daniel Mercer</p>
      <div class="person__role-row">
        <p class="person__role">Managing Director</p>
        <span class="person__rule"></span>
      </div>
    </div>

    <ul class="contact">
      <li class="contact__item">
        <svg class="contact__icon" viewBox="0 0 16 16" aria-hidden="true">
          <path d="M3.5 1.5l2.3 2.6-1.3 1.7c.9 2 2.6 3.7 4.6 4.6l1.7-1.3 2.6 2.3-1.4 2c-5.4-.4-9.9-4.9-10.3-10.3z" fill="none" stroke="var(--brand-green)" stroke-width="1.6" stroke-linejoin="round"/>
          <path d="M9.5 2.5a4.5 4.5 0 0 1 4 4M9.3 4.8a2.3 2.3 0 0 1 1.9 1.9" fill="none" stroke="var(--brand-green)" stroke-width="1.4" stroke-linecap="round"/>
        </svg>
        044-555 210 347
      </li>
      <li class="contact__item">
        <svg class="contact__icon" viewBox="0 0 16 16" aria-hidden="true">
          <rect x="0.5" y="3" width="15" height="10" fill="var(--brand-green)"/>
          <path d="M0.5 3.5l7.5 5.5 7.5-5.5M0.5 12.5l5.5-4.5M15.5 12.5l-5.5-4.5" fill="none" stroke="#ffffff" stroke-width="1.1"/>
        </svg>
        info@brightfieldyard.com
      </li>
      <li class="contact__item">
        <svg class="contact__icon" viewBox="0 0 16 16" aria-hidden="true">
          <g fill="none" stroke="var(--brand-green)" stroke-width="1.3">
            <circle cx="8" cy="8" r="6.8"/>
            <ellipse cx="8" cy="8" rx="3" ry="6.8"/>
            <path d="M1.2 8h13.6M2.2 4.6h11.6M2.2 11.4h11.6"/>
          </g>
        </svg>
        <span>www.<span class="contact__highlight">brightfieldyard</span>.com</span>
      </li>
    </ul>

    <address class="address">78 Orchard Lane, North Block<br>60718, Springdale</address>
  </section>

  <section class="card card--back" aria-label="Business card back">
    <h2 class="brand">
      <span class="brand__primary">BRIGHTFIELD</span>
      <span class="brand__secondary">YARD SERVICE AND BEYOND LLC</span>
    </h2>
    <p class="tagline">Licensed and insured</p>

    <p class="services">
      • Mowing • Weed eating • Edging • Hedge trimming<br>
      • Landscaping • Mulching • Yard clean up • Pressure washing
    </p>

    <div class="grass-band" role="img" aria-label="Row of grass blades along the bottom edge"></div>
  </section>

</body>
</html>
```